Business card design needed

Brenlo First Aid Training is a training provider in the Canberra region. We provide both public and private course bookings.

I want my business card to be fun/interesting. I have attached my own logo, however whatever you think works best will work for me.

Please see my website for more inspiration at www.brenlo-example.com.au

I would like a double sided design, and round corners please.

Some really good designs so far, just not quite the right one yet. 
Please look at my website for inspiration. 
Www.brenlo-example.com.au

Industry/Entity Type

Training

Contact Information for Business Card

Brenlo First Aid Training, Tobin Marsh, 0498563027, tobinmarsh4@mailvex-example.com.au, www.brenlo-example.com.au

```html
<!DOCTYPE html>
<html lang="en">
<head>
<meta charset="utf-8">
<title>Brenlo First Aid Training – Business Card</title>
<link rel="stylesheet" href="https://fonts.googleapis.com/css2?family=Archivo+Black&family=Arimo:wght@400&family=Kaushan+Script&display=swap">
<style>
  :root {
    --page-bg: #e6e8ec;
    --card-navy: #142a50;
    --ring-navy: #0f2146;
    --teal-deep: #0a5f82;
    --teal-mid: #1686b8;
    --teal-light: #2aa7d6;
    --edge-light: #7fd0f0;
    --text-white: #ffffff;
    --steel-light: #e4e6e9;
    --steel-dark: #7d8289;
  }
  * { margin: 0; padding: 0; box-sizing: border-box; }
  html, body {
    width: 1200px;
    height: 894px;
    overflow: hidden;
    background: var(--page-bg);
  }
  .card {
    position: absolute;
    left: 100px;
    top: 157px;
    width: 1000px;
    height: 580px;
    border-radius: 28px;
    overflow: hidden;
    background: var(--card-navy);
    box-shadow: 0 10px 30px rgba(0, 0, 0, 0.25);
  }
  .card-shapes {
    position: absolute;
    inset: 0;
  }
  .brand-name {
    position: absolute;
    left: 45px;
    top: 118px;
    width: 200px;
    text-align: center;
    font-family: "Archivo Black", sans-serif;
    font-size: 40px;
    color: var(--text-white);
  }
  .title {
    position: absolute;
    left: 442px;
    top: 130px;
    font-family: "Archivo Black", sans-serif;
    font-size: 74px;
    letter-spacing: 1px;
    color: var(--text-white);
  }
  .tagline {
    position: absolute;
    left: 336px;
    top: 238px;
    width: 620px;
    font-family: "Kaushan Script", cursive;
    font-size: 38px;
    letter-spacing: 1.5px;
    color: var(--text-white);
    white-space: nowrap;
  }
  .contact {
    position: absolute;
    left: 340px;
    top: 302px;
    width: 560px;
    text-align: center;
    font-family: "Arimo", sans-serif;
    font-size: 20px;
    letter-spacing: 1.5px;
    line-height: 28px;
    color: var(--text-white);
  }
  .stethoscope-art {
    position: absolute;
    left: 513px;
    top: 470px;
    width: 300px;
    height: 110px;
    border-radius: 60px 60px 0 0;
    background: linear-gradient(180deg, var(--steel-light), var(--steel-dark));
    opacity: 0.85;
  }
</style>
</head>
<body>
  <div class="card">
    <svg class="card-shapes" width="1000" height="580" viewBox="0 0 1000 580" aria-hidden="true">
      <defs>
        <linearGradient id="band-fill" x1="0" y1="0" x2="0" y2="1">
          <stop offset="0" stop-color="var(--teal-mid)"/>
          <stop offset="1" stop-color="var(--teal-deep)"/>
        </linearGradient>
        <radialGradient id="disc-fill" cx="0.5" cy="0.5" r="0.5">
          <stop offset="0" stop-color="var(--teal-deep)"/>
          <stop offset="0.6" stop-color="var(--teal-mid)"/>
          <stop offset="1" stop-color="var(--teal-light)"/>
        </radialGradient>
        <radialGradient id="chest-fill" cx="0.5" cy="0.5" r="0.5">
          <stop offset="0" stop-color="#05253a"/>
          <stop offset="0.55" stop-color="var(--teal-deep)"/>
          <stop offset="1" stop-color="var(--teal-light)"/>
        </radialGradient>
      </defs>
      <path class="side-band" d="M0 0 H290 C345 80 340 220 270 285 C195 355 110 420 92 580 H0 Z" fill="url(#band-fill)"/>
      <path class="side-band-edge" d="M270 285 C195 355 110 420 92 580" fill="none" stroke="var(--edge-light)" stroke-width="3"/>
      <circle class="logo-ring-outer" cx="145" cy="143" r="205" fill="var(--teal-mid)"/>
      <circle class="logo-ring" cx="145" cy="143" r="192" fill="var(--ring-navy)"/>
      <circle class="logo-disc" cx="145" cy="143" r="176" fill="url(#disc-fill)"/>
      <circle class="chest-ring" cx="970" cy="500" r="142" fill="var(--teal-mid)"/>
      <circle class="chest-disc" cx="970" cy="500" r="128" fill="url(#chest-fill)"/>
    </svg>

    <div class="brand-name">Brenlo</div>

    <h1 class="title">Brenlo</h1>
    <p class="tagline">First Aid Training, Tobin Marsh,</p>
    <p class="contact">0498563027, tobinmarsh4@mailvex-example.com.au,<br>www.brenlo-example.com.au</p>

    <div class="stethoscope-art" role="img" aria-label="Stethoscope tubing illustration"></div>
  </div>
</body>
</html>
```